依頼概要
■依頼の目的/概要
弊社の社員が着用する名札のデザインをお願いします。

■依頼詳細
社員全員が着用する名札を制作しようと考えております。
名札の素材はアクリルで検討していますが、デザインによって2層タイプのものにしたり、着色したりすることも検討しています。
名札はピン2本で固定しようと考えております。
名札を着用する服は、白のワイシャツ、白のブラウス及び緑色の作業ジャンパーです。

■デザインに必須の情報
名札に載せてほしい情報は、会社のロゴ、会社名及び個人の氏名です。
会社のロゴ及び社名は添付のファイルを参考にしてください。

■デザインに関する要望
シャープでかっちりした感じ、先進的な感じにしていただきたいです。

■弊社のご紹介
弊社は創業108年の住宅用資材を工務店や建設会社に販売する会社です。資材の販売を中心として、建築業界の生産性を向上させるためのシステム開発、各種教育システムの開発、地域の建築業界活性化に資する書籍の出版なども行っております。
社員数は100名、年商30億円の会社です。

その他何かご不明な点がございましたら、お気軽にご質問下さい。
よろしくお願いいたします。

シンプルながらしっかり我が社のイメージも出してくれるからです。しかも作業服に取り付ける場合のワッペンとしても作りやすいデザインでした。

短期間にもかかわらずたくさんのご提案ありがとうございました。
またいろいろとよろしくお願いします。

```html
<!DOCTYPE html>
<html lang="ja">
<head>
<meta charset="utf-8">
<title>名札デザイン 株式会社 創栄</title>
<link rel="stylesheet" href="https://fonts.googleapis.com/css2?family=Noto+Sans+JP:wght@500;700&family=Tinos:ital@1&display=swap">
<style>
  :root {
    --page-bg: #ffffff;
    --brand-green: #1f8a3a;
    --green-dark: #137a2e;
    --green-light: #5bb85e;
    --silver-dark: #b9b9b9;
    --silver-light: #f2f2f2;
    --silver-mark: #e6e6e6;
    --ink: #111111;
    --paper: #ffffff;
    --edge: #9a9a9a;
  }
  html, body {
    margin: 0;
    padding: 0;
    width: 732px;
    height: 1200px;
    overflow: hidden;
    background: var(--page-bg);
  }
  .sheet {
    position: relative;
    width: 732px;
    height: 1200px;
  }
  .badge {
    position: absolute;
    left: 54px;
    width: 624px;
    height: 251px;
    border-radius: 24px;
    box-sizing: border-box;
    border: 2px solid var(--edge);
    font-family: "Noto Sans JP", sans-serif;
  }
  .badge--white { top: 37px; background: var(--paper); color: var(--ink); }
  .badge--green {
    top: 478px;
    border-color: var(--green-dark);
    background: linear-gradient(100deg, var(--green-dark) 0%, var(--green-light) 55%, var(--green-dark) 100%);
    color: var(--paper);
  }
  .badge--silver {
    top: 903px;
    background: linear-gradient(100deg, var(--silver-dark) 0%, var(--silver-light) 50%, var(--silver-dark) 100%);
    color: var(--ink);
  }
  .company {
    position: absolute;
    left: 40px;
    top: 26px;
    width: 200px;
    text-align: center;
  }
  .company__dot {
    display: block;
    width: 96px;
    height: 96px;
    margin: 0 auto 14px;
    border-radius: 50%;
    background: var(--brand-green);
  }
  .company__name {
    font-weight: 700;
    font-size: 34px;
    letter-spacing: 2px;
    color: var(--brand-green);
    white-space: nowrap;
  }
  .badge--green .company__dot { background: var(--paper); }
  .badge--green .company__name { color: var(--paper); }
  .badge--silver .company__dot { background: var(--silver-mark); }
  .badge--silver .company__name { color: var(--silver-mark); }
  .person {
    position: absolute;
    left: 307px;
    top: 28px;
  }
  .person__dept {
    font-weight: 700;
    font-size: 26px;
    letter-spacing: 6px;
    margin: 0;
  }
  .person__name {
    font-weight: 700;
    font-size: 50px;
    letter-spacing: 4px;
    margin: 14px 0 0;
    line-height: 1.1;
  }
  .person__roman {
    font-family: "Tinos", serif;
    font-style: italic;
    font-size: 32px;
    margin: 6px 0 0;
  }
</style>
</head>
<body>
<main class="sheet">
  <section class="badge badge--white">
    <div class="company"><span class="company__dot"></span><div class="company__name">株式会社 創栄</div></div>
    <div class="person">
      <p class="person__dept">工事課</p>
      <p class="person__name">山田 太郎</p>
      <p class="person__roman">Taro Yamada</p>
    </div>
  </section>
  <section class="badge badge--green">
    <div class="company"><span class="company__dot"></span><div class="company__name">株式会社 創栄</div></div>
    <div class="person">
      <p class="person__dept">工事課</p>
      <p class="person__name">山田 太郎</p>
      <p class="person__roman">Taro Yamada</p>
    </div>
  </section>
  <section class="badge badge--silver">
    <div class="company"><span class="company__dot"></span><div class="company__name">株式会社 創栄</div></div>
    <div class="person">
      <p class="person__dept">工事課</p>
      <p class="person__name">山田 太郎</p>
      <p class="person__roman">Taro Yamada</p>
    </div>
  </section>
</main>
</body>
</html>
```